Business Card Design

Electronic Security
Alarm Systems
CCTV
Electronic Access Control
Security System Integration

Industry/Entity Type

Business

Contact Information for Business Card

Gareth Linwood
PO Box 862
Yarrowdale Qld 4173
Phone 07 38265140
Mob 0428637291

```html
<!DOCTYPE html>
<html lang="en">
<head>
<meta charset="utf-8">
<title>Business Card – Gareth Linwood</title>
<link rel="stylesheet" href="https://fonts.googleapis.com/css2?family=Open+Sans:wght@400;600&display=swap">
<style>
  :root {
    --page: #ece8e1;
    --card: #ffffff;
    --slate-dark: #343d46;
    --slate-light: #4f8197;
    --sun-light: #fdd526;
    --sun-dark: #f5b51c;
    --sky-light: #3aa9e2;
    --sky-dark: #2590cf;
    --ink: #2b3640;
    --on-colour: #ffffff;
  }
  * { margin: 0; padding: 0; box-sizing: border-box; }
  html, body {
    width: 1200px; height: 1000px; overflow: hidden;
    background: var(--page);
    font-family: "Open Sans", sans-serif;
  }
  .card {
    position: absolute; left: 150px; top: 245px;
    width: 900px; height: 510px;
    background: var(--card);
    box-shadow: 0 14px 40px rgba(0,0,0,.18);
    overflow: hidden;
  }
  .card-graphic { position: absolute; inset: 0; }
  .holder-name {
    position: absolute; left: 448px; top: 78px;
    color: var(--on-colour); font-size: 30px; font-weight: 400; letter-spacing: .3px;
  }
  .contact-list {
    position: absolute; left: 448px; top: 196px;
    list-style: none; color: var(--on-colour); font-size: 19px; line-height: 1.3;
  }
  .contact-list li { display: flex; align-items: flex-start; gap: 12px; margin-bottom: 10px; }
  .contact-list svg { width: 20px; height: 20px; flex: none; margin-top: 3px; fill: var(--on-colour); }
  .brand {
    position: absolute; left: 70px; bottom: 62px;
    display: flex; align-items: center; gap: 16px;
  }
  .brand-dot { width: 34px; height: 34px; border-radius: 50%; background: var(--sky-dark); }
  .brand-name { font-size: 44px; font-weight: 400; color: var(--ink); letter-spacing: 1px; }
</style>
</head>
<body>
  <article class="card">
    <svg class="card-graphic" viewBox="0 0 900 510" width="900" height="510" aria-hidden="true">
      <defs>
        <linearGradient id="slate" x1="0" y1="1" x2="1" y2="0">
          <stop offset="0" stop-color="var(--slate-dark)"/>
          <stop offset="1" stop-color="var(--slate-light)"/>
        </linearGradient>
        <linearGradient id="sun" x1="0" y1="0" x2="1" y2="1">
          <stop offset="0" stop-color="var(--sun-light)"/>
          <stop offset="1" stop-color="var(--sun-dark)"/>
        </linearGradient>
        <linearGradient id="sky" x1="0" y1="1" x2="1" y2="0">
          <stop offset="0" stop-color="var(--sky-dark)"/>
          <stop offset="1" stop-color="var(--sky-light)"/>
        </linearGradient>
      </defs>
      <polygon class="band-slate" fill="url(#slate)" points="420,0 640,0 700,170 420,150"/>
      <polygon class="band-sun" fill="url(#sun)" points="640,0 900,0 900,120 700,170"/>
      <polygon class="band-sky" fill="url(#sky)" points="420,150 700,170 900,120 900,340 420,340"/>
    </svg>

    <h1 class="holder-name">Gareth Linwood</h1>

    <ul class="contact-list">
      <li>
        <svg viewBox="0 0 24 24"><path d="M3 8c0-2 2-4 9-4s9 2 9 4v2h-5V8c-1-.6-2.4-1-4-1s-3 .4-4 1v2H3zM5 12h14l1 8H4z"/></svg>
        <span>07 38265140</span>
      </li>
      <li>
        <svg viewBox="0 0 24 24"><path d="M6.6 10.8a15 15 0 0 0 6.6 6.6l2.2-2.2a1 1 0 0 1 1-.25 11.4 11.4 0 0 0 3.6.6 1 1 0 0 1 1 1V20a1 1 0 0 1-1 1A17 17 0 0 1 3 4a1 1 0 0 1 1-1h3.5a1 1 0 0 1 1 1c0 1.25.2 2.45.6 3.6a1 1 0 0 1-.25 1z"/></svg>
        <span>0428637291</span>
      </li>
      <li>
        <svg viewBox="0 0 24 24"><path d="M12 2a7 7 0 0 0-7 7c0 5.25 7 13 7 13s7-7.75 7-13a7 7 0 0 0-7-7zm0 9.5A2.5 2.5 0 1 1 12 6.5a2.5 2.5 0 0 1 0 5z"/></svg>
        <span>PO Box 862<br>Yarrowdale Qld 4173</span>
      </li>
    </ul>

    <div class="brand">
      <span class="brand-dot"></span>
      <span class="brand-name">Norvane</span>
    </div>
  </article>
</body>
</html>
```